Design 6.5 x 9 Postcard for Business

You will need to design a 6.5" x 9" postcard for our insulation business, Brightfold Energy, LLC based on design requirements. We will be using PostRiver and have attached template for guide. Must include phone number, web address, company logo, warm haven partner logo and marketing call to action. Specificallyl marketing 75-100% off insulation & weatheriation services with FREE Home Energy Assessment. Absolutely no cost. I have given examples of other companies on attachment as well for inspiration. I will also need to ensure that somewhere clear is "Our company just insulated a home on your mail route and we'd like to offer you a FREE assessment!"

Here are competitior websites for inspiration.

https://www.lumatekpower.example/?gclid=XbTqRwLmPz8KdYhNvCu3-FJe2WQSaLpOkMxGyH_ZtUeR

https://www.tidalnestpower.example/

```html
<!DOCTYPE html>
<html lang="en">
<head>
<meta charset="utf-8">
<title>Brightfold Energy Postcard Options</title>
<link rel="stylesheet" href="https://fonts.googleapis.com/css2?family=Oswald:wght@600&family=Hind:wght@300;400;500;600;700&family=Quicksand:wght@500;600;700&display=swap">
<style>
  :root{
    --board:#464a4e;
    --navy:#0b4a83;
    --cyan:#14c9ea;
    --slate:#7f8083;
    --panel-gray:#808184;
    --white:#ffffff;
    --ink:#2f3135;
    --sky-top:#a9c6e6;
    --sky-low:#dbe7f3;
    --wood:#b7772e;
    --wood-dark:#7a4a1a;
  }
  *{box-sizing:border-box;margin:0;padding:0}
  html,body{width:1200px;height:902px;overflow:hidden;background:var(--board)}
  .board{position:relative;width:1200px;height:902px;font-family:"Hind",sans-serif}
  .option-title{position:absolute;top:78px;width:300px;text-align:center;color:var(--white);font:600 24px/1 "Hind",sans-serif;letter-spacing:.5px}
  .divider{position:absolute;left:602px;top:74px;width:1px;height:758px;background:#c9cbcd}
  .card{position:absolute;width:445px;height:328px;overflow:hidden;background:var(--white);box-shadow:8px 10px 10px rgba(0,0,0,.35)}
  .abs{position:absolute}
  .center{left:0;width:100%;text-align:center}

  .brand-mark{position:absolute;display:flex;align-items:center;gap:5px;color:var(--navy);font:600 12px/1 "Hind",sans-serif;letter-spacing:.8px;white-space:nowrap}
  .brand-mark .brand-square{width:9px;height:9px;border:2px solid var(--navy)}

  /* option 1 front */
  .front-classic .blue-field{position:absolute;left:0;top:0;width:445px;height:277px;background:var(--navy)}
  .discount-line{top:38px;color:var(--white);font:600 74px/1 "Oswald",sans-serif;letter-spacing:-.5px;white-space:nowrap}
  .discount-line .pct{font-size:34px;vertical-align:26px;margin-left:1px}
  .discount-line .off{font-size:38px}
  .service-line{top:120px;color:var(--white);font:500 16.5px/1 "Hind",sans-serif;letter-spacing:.2px}
  .season-tile{position:absolute;top:153px;width:65px;height:65px;border-radius:6px;display:flex;align-items:center;justify-content:center}
  .season-tile.cyan{background:var(--cyan)}
  .season-tile.slate{background:var(--slate)}
  .route-note{color:var(--white);font:400 9.3px/11.5px "Hind",sans-serif}
  .route-note b{font-weight:700}

  /* back panels */
  .offer-block{position:absolute;top:0;width:258px;height:328px;text-align:center}
  .free-word{font:700 55px/1 "Hind",sans-serif;letter-spacing:1px}
  .assess-line{font:500 19.5px/1 "Hind",sans-serif}
  .no-cost{font:300 14.5px/1 "Hind",sans-serif;letter-spacing:.3px}
  .partner-label{font:400 10.5px/1 "Hind",sans-serif}
  .partner-badge{position:absolute;width:62px;height:34px;border-radius:4px}
  .cta-line{font:600 12.5px/1 "Hind",sans-serif}
  .contact-row{display:flex;justify-content:center;align-items:center;gap:6px;font:400 11px/1 "Hind",sans-serif}
  .contact-row .sep{width:1px;height:16px}
  .stamp-box{position:absolute;width:45px;height:33px;border:1px solid #9a9ca0;background:var(--white)}
  .address-stars{position:absolute;font:400 6px/1 "Hind",sans-serif;color:var(--ink);letter-spacing:-.3px;white-space:nowrap;overflow:hidden}
  .address-lines{position:absolute;font:400 5px/6.5px "Hind",sans-serif;color:var(--ink)}

  .back-classic .offer-block{left:0;color:var(--navy)}
  .back-classic .partner-badge{background:#6aa93a}
  .back-classic .contact-row .sep{background:#9fa3a8}
  .back-classic .mail-rule{position:absolute;left:247px;top:33px;width:1px;height:262px;background:#9fa3a8}

  .back-modern .offer-block{left:-3px;color:var(--white)}
  .back-modern .partner-badge{background:#d9dadc}
  .back-modern .contact-row .sep{background:#c9cacc}

  /* option 2 front */
  .front-modern{background:var(--navy)}
  .big-figure{position:absolute;color:var(--white);font:500 62px/1 "Quicksand",sans-serif;white-space:nowrap}
  .big-figure .pct{font-size:30px;vertical-align:24px;margin-left:2px}
  .big-figure .word{font-size:37px;margin-left:10px}
  .big-figure .off{font-size:29px}
  .modern-service{color:var(--white);font:500 16.5px/20px "Hind",sans-serif}
</style>
</head>
<body>
<div class="board">
  <div class="option-title" style="left:146px">OPTION 1</div>
  <div class="option-title" style="left:739px">OPTION 2</div>
  <div class="divider"></div>

  <!-- Option 1 front -->
  <section class="card front-classic" style="left:89px;top:145px">
    <div class="blue-field"></div>
    <div class="abs center discount-line">75<span class="pct">%</span>-100<span class="pct">%</span><span class="off">OFF</span></div>
    <div class="abs center service-line">INSULATION &amp; WEATHERIATION SERVICES.</div>

    <div class="season-tile cyan" style="left:79px">
      <svg width="44" height="44" viewBox="0 0 44 44" fill="none" stroke="#fff" stroke-width="2" stroke-linecap="round">
        <circle cx="22" cy="22" r="8"/>
        <path d="M22 3v7M22 34v7M3 22h7M34 22h7M8.5 8.5l5 5M30.5 30.5l5 5M8.5 35.5l5-5M30.5 13.5l5-5"/>
      </svg>
    </div>
    <div class="season-tile slate" style="left:153px">
      <svg width="44" height="44" viewBox="0 0 44 44" fill="none" stroke="#fff" stroke-width="2" stroke-linejoin="round" stroke-linecap="round">
        <path d="M22 5C12 13 9 22 13 30c3 5 15 5 18 0 4-8 1-17-9-25z"/>
        <path d="M22 12v30M22 22l-6-5M22 22l6-5M22 29l-7-5M22 29l7-5"/>
      </svg>
    </div>
    <div class="season-tile cyan" style="left:227px">
      <svg width="44" height="44" viewBox="0 0 44 44" fill="none" stroke="#fff" stroke-width="2">
        <circle cx="22" cy="22" r="6"/>
        <circle cx="22" cy="11" r="6"/><circle cx="22" cy="33" r="6"/>
        <circle cx="11" cy="22" r="6"/><circle cx="33" cy="22" r="6"/>
      </svg>
    </div>
    <div class="season-tile slate" style="left:301px">
      <svg width="44" height="44" viewBox="0 0 44 44" fill="none" stroke="#fff" stroke-width="2.4" stroke-linecap="round">
        <path d="M22 4v36M6.4 13l31.2 18M6.4 31l31.2-18"/>
        <path d="M17 8l5 5 5-5M17 36l5-5 5 5M8 20l7 2-2 7M36 20l-7 2 2 7M8 24l7-2M36 24l-7-2"/>
      </svg>
    </div>

    <p class="abs center route-note" style="top:233px">Our company just insulated a home on your mail route<br>and we'd like to offer you a <b>FREE assessment!</b></p>

    <div class="brand-mark" style="left:0;width:445px;justify-content:center;top:296px"><span class="brand-square"></span>BRIGHTFOLD</div>
  </section>

  <!-- Option 1 back -->
  <section class="card back-classic" style="left:89px;top:505px">
    <div class="offer-block">
      <div class="abs center free-word" style="top:35px">FREE</div>
      <div class="abs center assess-line" style="top:81px">HOME ENERGY</div>
      <div class="abs center assess-line" style="top:102px">ASSESSMENT.</div>
      <div class="abs center no-cost" style="top:131px">ABSOLUTELY NO COST.</div>
      <div class="abs center partner-label" style="top:169px">In partnership with:</div>
      <div class="partner-badge" role="img" aria-label="warm haven partner badge" style="left:98px;top:185px"></div>
      <div class="abs center cta-line" style="top:258px">Get your free assessment now!</div>
      <div class="abs center contact-row" style="top:275px">
        <svg width="11" height="11" viewBox="0 0 24 24" fill="none" stroke="currentColor" stroke-width="2"><path d="M5 3h4l2 5-3 2a12 12 0 006 6l2-3 5 2v4a2 2 0 01-2 2A18 18 0 013 5a2 2 0 012-2z"/></svg>
        <span>555-014-2276</span><span class="sep"></span>
        <svg width="11" height="11" viewBox="0 0 24 24" fill="none" stroke="currentColor" stroke-width="2"><circle cx="12" cy="12" r="10"/><ellipse cx="12" cy="12" rx="4" ry="10"/><path d="M2 12h20"/></svg>
        <span>brightfold.example</span>
      </div>
    </div>
    <div class="mail-rule"></div>
    <div class="brand-mark" style="left:330px;top:38px"><span class="brand-square"></span>BRIGHTFOLD</div>
    <div class="stamp-box" style="left:377px;top:227px"></div>
    <div class="address-stars" style="left:293px;top:265px;width:130px">****************************************************</div>
    <div class="address-lines" style="left:293px;top:277px">Local<br>Postal Customer</div>
  </section>

  <!-- Option 2 front -->
  <section class="card front-modern" style="left:662px;top:145px">
    <svg class="abs" style="left:0;top:0" width="445" height="328" viewBox="0 0 445 328">
      <defs>
        <linearGradient id="sky-to-wood" x1="0" y1="0" x2="0.35" y2="1">
          <stop offset="0" stop-color="var(--sky-top)"/>
          <stop offset="0.45" stop-color="var(--sky-low)"/>
          <stop offset="0.62" stop-color="var(--wood)"/>
          <stop offset="1" stop-color="var(--wood-dark)"/>
        </linearGradient>
      </defs>
      <polygon points="294,0 445,0 445,328 333,328 238,127" fill="url(#sky-to-wood)" role="img" aria-label="Photo of a timber-clad house gable against a blue sky"/>
      <polyline points="287,0 230,127 323,328" fill="none" stroke="#fff" stroke-width="3"/>
      <polyline points="250,60 211,120 243,168" fill="none" stroke="#7f8083" stroke-width="11" stroke-linejoin="miter"/>
    </svg>
    <div class="brand-mark" style="right:22px;top:36px"><span class="brand-square"></span>BRIGHTFOLD</div>
    <div class="big-figure" style="left:33px;top:50px">75<span class="pct">%</span><span class="word">TO</span></div>
    <div class="big-figure" style="left:29px;top:113px">100<span class="pct">%</span><span class="off">OFF</span></div>
    <div class="abs modern-service" style="left:33px;top:180px">Insulation &amp; weatheriation<br>services.</div>
    <p class="abs route-note" style="left:33px;top:264px;font-size:8.8px;line-height:11px">Our company just insulated a home on your mail route<br>and we'd like to offer you a <b>FREE assessment!</b></p>
  </section>

  <!-- Option 2 back -->
  <section class="card back-modern" style="left:662px;top:505px">
    <svg class="abs" style="left:0;top:0" width="445" height="328" viewBox="0 0 445 328">
      <polygon points="0,0 239,0 286,127 239,328 0,328" fill="var(--panel-gray)"/>
      <polyline points="244,0 293,127 244,328" fill="none" stroke="var(--navy)" stroke-width="4"/>
    </svg>
    <div class="offer-block">
      <div class="abs center free-word" style="top:32px">FREE</div>
      <div class="abs center assess-line" style="top:78px">HOME ENERGY</div>
      <div class="abs center assess-line" style="top:97px">ASSESSMENT.</div>
      <div class="abs center no-cost" style="top:125px">ABSOLUTELY NO COST.</div>
      <div class="abs center partner-label" style="top:167px">In partnership with:</div>
      <div class="partner-badge" role="img" aria-label="warm haven partner badge" style="left:98px;top:185px"></div>
      <div class="abs center cta-line" style="top:258px">Get your free assessment now!</div>
      <div class="abs center contact-row" style="top:277px">
        <svg width="11" height="11" viewBox="0 0 24 24" fill="none" stroke="currentColor" stroke-width="2"><path d="M5 3h4l2 5-3 2a12 12 0 006 6l2-3 5 2v4a2 2 0 01-2 2A18 18 0 013 5a2 2 0 012-2z"/></svg>
        <span>555-014-2276</span><span class="sep"></span>
        <svg width="11" height="11" viewBox="0 0 24 24" fill="none" stroke="currentColor" stroke-width="2"><circle cx="12" cy="12" r="10"/><ellipse cx="12" cy="12" rx="4" ry="10"/><path d="M2 12h20"/></svg>
        <span>brightfold.example</span>
      </div>
    </div>
    <div class="brand-mark" style="right:28px;top:38px"><span class="brand-square"></span>BRIGHTFOLD</div>
    <div class="stamp-box" style="left:378px;top:227px"></div>
    <div class="address-stars" style="left:293px;top:265px;width:131px">****************************************************</div>
    <div class="address-lines" style="left:293px;top:277px">Local<br>Postal Customer</div>
  </section>
</div>
</body>
</html>
```